Facebook Page Design for a Medical Billing Business

We need help designing a facebook page that is professional, yet friendly that will attract medical practitioners (doctors, therapists, nutritionists, chiropractors, etc) to check out and follow our business. I have attached our logo which must be incorporated in the design.

```html
<!DOCTYPE html>
<html lang="en">
<head>
<meta charset="utf-8">
<title>Vega Medical Billing – Page Cover</title>
<link rel="stylesheet" href="https://fonts.googleapis.com/css2?family=Tinos:wght@400;700&display=swap">
<style>
  :root {
    --page-bg: #ebedf0;
    --space-deep: #140a3a;
    --space-violet: #4a1a7a;
    --space-magenta: #9a1a8c;
    --text-white: #ffffff;
    --accent-blue: #21a9ea;
    --ring-pink: #e0259a;
    --ring-blue: #1aa6ee;
    --mark-violet: #b34fd8;
  }
  * { margin: 0; padding: 0; box-sizing: border-box; }
  html, body {
    width: 1200px; height: 800px; overflow: hidden;
    background: var(--page-bg);
    font-family: "Tinos", "Times New Roman", serif;
  }
  .canvas { position: relative; width: 1200px; height: 800px; }

  .profile-badge {
    position: absolute; left: 69px; top: 79px;
    width: 188px; height: 188px; border-radius: 50%;
    background: linear-gradient(135deg, var(--ring-pink), #7a4fd8 55%, var(--ring-blue));
    padding: 4px;
  }
  .profile-badge__inner {
    width: 100%; height: 100%; border-radius: 50%;
    background: #000;
    display: flex; flex-direction: column; align-items: center; justify-content: center;
    text-align: center;
  }
  .brand-name {
    color: var(--mark-violet); font-weight: 400; line-height: 1;
  }
  .profile-badge .brand-name__main { font-size: 34px; letter-spacing: 2px; }
  .profile-badge .brand-name__sub { font-size: 8px; letter-spacing: 2px; margin-top: 6px; }

  .cover {
    position: absolute; left: 273px; top: 60px;
    width: 857px; height: 326px; overflow: hidden;
    color: var(--text-white); text-align: center;
  }
  .cover__backdrop {
    position: absolute; inset: 0;
    background:
      radial-gradient(ellipse 40% 45% at 8% 60%, rgba(200,30,160,.75), transparent 70%),
      radial-gradient(ellipse 35% 30% at 30% 105%, rgba(190,40,200,.9), transparent 70%),
      radial-gradient(ellipse 35% 45% at 90% 25%, rgba(140,50,180,.55), transparent 70%),
      linear-gradient(180deg, var(--space-violet), var(--space-deep));
  }
  .cover__content { position: absolute; inset: 0; }

  .cover .brand-name { color: var(--text-white); position: absolute; left: 0; right: 0; top: 70px; }
  .cover .brand-name__main { display: block; font-size: 44px; letter-spacing: 3px; }
  .cover .brand-name__sub { display: block; font-size: 10px; letter-spacing: 4px; margin-top: 4px; }

  .cover__title {
    position: absolute; left: 0; right: 0; top: 164px;
    font-size: 43px; font-weight: 400; letter-spacing: .5px;
  }
  .cover__tagline {
    position: absolute; left: 0; right: 0; top: 216px;
    display: flex; align-items: center; justify-content: center; gap: 10px;
    color: var(--accent-blue); font-size: 17px;
  }
  .cover__tagline::before, .cover__tagline::after {
    content: ""; width: 80px; height: 1px; background: var(--accent-blue);
  }
  .cover__cta {
    position: absolute; left: 50%; top: 256px; transform: translateX(-50%);
    border: 1.5px solid var(--text-white); border-radius: 8px;
    color: var(--accent-blue); font-weight: 700; font-size: 12px;
    padding: 1px 7px;
  }
  .cover__contacts {
    position: absolute; left: 0; right: 0; top: 289px;
    display: flex; justify-content: center; gap: 10px;
    font-size: 16px;
  }
  .contact-item { display: flex; align-items: center; gap: 4px; }
  .contact-item svg { width: 15px; height: 15px; }
</style>
</head>
<body>
<main class="canvas">
  <div class="profile-badge">
    <div class="profile-badge__inner">
      <p class="brand-name">
        <span class="brand-name__main">VEGA</span><br>
        <span class="brand-name__sub">MEDICAL BILLING</span>
      </p>
    </div>
  </div>

  <section class="cover">
    <div class="cover__backdrop" role="img" aria-label="Starry purple and magenta night sky with glowing planets and shooting stars"></div>
    <div class="cover__content">
      <p class="brand-name">
        <span class="brand-name__main">VEGA</span>
        <span class="brand-name__sub">MEDICAL BILLING</span>
      </p>
      <h1 class="cover__title">VEGA MEDICAL BILLING, LLC</h1>
      <p class="cover__tagline">Medical Billing Tailored To Your Practices Needs</p>
      <span class="cover__cta">Contact Now</span>
      <p class="cover__contacts">
        <span class="contact-item">
          <svg viewBox="0 0 16 16" aria-hidden="true"><rect x=".75" y=".75" width="14.5" height="14.5" rx="2" fill="none" stroke="#21a9ea" stroke-width="1.5"/><path d="M5 3.5l2 2-1 1.2c.6 1.3 1.6 2.3 2.9 2.9L10 8.6l2 2-1.3 1.5C7.5 12 4 8.5 3.5 5z" fill="#21a9ea"/></svg>
          425-555-0188
        </span>
        <span class="contact-item">
          <svg viewBox="0 0 16 16" aria-hidden="true"><rect x=".75" y=".75" width="14.5" height="14.5" rx="2" fill="none" stroke="#21a9ea" stroke-width="1.5"/><path d="M5 3v9l2.3-2.2 1.6 3.2 1.4-.7-1.6-3.1H12z" fill="#21a9ea"/></svg>
          www.vegamedicalbilling.com
        </span>
        <span class="contact-item">
          <svg viewBox="0 0 16 16" aria-hidden="true"><rect x=".75" y="2.75" width="14.5" height="10.5" rx="1" fill="none" stroke="#21a9ea" stroke-width="1.5"/><path d="M1.5 3.5l6.5 5 6.5-5" fill="none" stroke="#21a9ea" stroke-width="1.5"/></svg>
          Admin@vegamedicalbilling.com
        </span>
      </p>
    </div>
  </section>
</main>
</body>
</html>
```